Graphic Design for Company Van - White Marlo Pivot Haulmate 2019 LWB

We are a Electronic Security Systems Company specializing in CCTV, Intruder Alarms, Fire Alarms, Access Control and Gate Automation.
I am looking for a modern design for a van wrap to include company logo, phone number, website, the types of work we do (CCTV ect), and our QLR Licence number, its specifically for the model of van in the project name mentioned above. I will attach some of our branded signage and siren logo with some more details. thank you.

```html
<!DOCTYPE html>
<html lang="en">
<head>
<meta charset="utf-8">
<title>Birch Guard – Van Wrap Side Panel</title>
<link rel="stylesheet" href="https://fonts.googleapis.com/css2?family=Lato:wght@400;700;900&display=swap">
<style>
  :root {
    --page: #f4f4f4;
    --wrap-white: #ffffff;
    --brand-red: #e43645;
    --band-dark: #333333;
    --photo-steel: #8fa3b8;
    --photo-deep: #3d4d5e;
    --camera-silver: #c9c9c9;
    --camera-dark: #2b2b2b;
    --ink: #111111;
    --icon-line: #ffffff;
  }
  html, body {
    margin: 0;
    padding: 0;
    width: 1200px;
    height: 645px;
    overflow: hidden;
    background: var(--page);
  }
  .wrap-panel {
    display: block;
    width: 1200px;
    height: 645px;
  }
  .brand-name {
    font-family: "Lato", sans-serif;
    font-weight: 700;
    font-size: 33px;
    fill: var(--ink);
  }
  .brand-tagline {
    font-family: "Lato", sans-serif;
    font-weight: 400;
    font-size: 15.5px;
    fill: var(--ink);
  }
  .phone-number {
    font-family: "Lato", sans-serif;
    font-weight: 700;
    font-size: 32px;
    fill: var(--brand-red);
  }
  .web-address {
    font-family: "Lato", sans-serif;
    font-weight: 700;
    font-size: 47px;
    fill: var(--wrap-white);
  }
  .service-icon circle {
    fill: none;
    stroke: var(--icon-line);
    stroke-width: 1.4;
  }
  .service-icon .glyph {
    fill: var(--icon-line);
  }
  .service-icon .glyph-line {
    fill: none;
    stroke: var(--icon-line);
    stroke-width: 1.6;
    stroke-linecap: round;
  }
</style>
</head>
<body>
<svg class="wrap-panel" viewBox="0 0 1200 645" xmlns="http://www.w3.org/2000/svg">
  <defs>
    <linearGradient id="photo-fade" x1="0" y1="0" x2="1" y2="0">
      <stop offset="0" stop-color="var(--band-dark)"/>
      <stop offset="0.25" stop-color="var(--photo-deep)"/>
      <stop offset="1" stop-color="var(--photo-steel)"/>
    </linearGradient>
    <radialGradient id="camera-tone" cx="0.45" cy="0.5" r="0.6">
      <stop offset="0" stop-color="var(--camera-dark)"/>
      <stop offset="0.55" stop-color="#555555"/>
      <stop offset="1" stop-color="var(--camera-silver)"/>
    </radialGradient>
    <clipPath id="panel-clip">
      <rect x="100" y="85" width="1010" height="380" rx="14"/>
    </clipPath>
  </defs>

  <g clip-path="url(#panel-clip)">
    <!-- base -->
    <rect class="panel-base" x="100" y="85" width="1010" height="380" fill="var(--wrap-white)"/>

    <!-- red top band -->
    <polygon class="red-band" points="689,85 1110,85 1110,168 890,182" fill="var(--brand-red)"/>

    <!-- dark lower band -->
    <polygon class="dark-band" points="100,420 900,235 1110,225 1110,465 100,465" fill="var(--band-dark)"/>

    <!-- warehouse photograph area -->
    <polygon class="photo-area" role="img" aria-label="Photograph of a large industrial warehouse interior"
             points="573,335 900,235 1110,225 1110,465 573,465" fill="url(#photo-fade)"/>

    <!-- security camera photograph area -->
    <rect class="camera-photo" role="img" aria-label="Photograph of a bullet CCTV security camera"
          x="890" y="130" width="220" height="210" rx="30" fill="url(#camera-tone)"/>
  </g>

  <!-- brand name -->
  <rect class="brand-square" x="660" y="172" width="24" height="24" fill="var(--brand-red)"/>
  <text class="brand-name" x="697" y="199">Birch Guard</text>
  <text class="brand-tagline" x="697" y="224">CCTV &amp; Alarm Installation</text>

  <!-- phone -->
  <text class="phone-number" x="336" y="310">0818 555 019</text>

  <!-- service icons -->
  <g class="service-icon icon-cctv" transform="translate(417 385)">
    <circle r="14"/>
    <rect class="glyph" x="-8" y="-5" width="12" height="6" rx="1" transform="rotate(20)"/>
    <path class="glyph-line" d="M-7 7 L-7 2 L-2 2"/>
  </g>
  <g class="service-icon icon-intruder" transform="translate(453 385)">
    <circle r="14"/>
    <rect class="glyph-line" x="-2" y="-8" width="8" height="16"/>
    <circle class="glyph" cx="-5" cy="-5" r="2" style="stroke:none"/>
    <path class="glyph-line" d="M-5 -2 L-4 3 L-7 8 M-4 3 L-1 7 M-8 0 L-2 0"/>
  </g>
  <g class="service-icon icon-siren" transform="translate(489 385)">
    <circle r="14"/>
    <path class="glyph" d="M-8 -3 L-4 -3 L1 -7 L1 7 L-4 3 L-8 3 Z"/>
    <path class="glyph-line" d="M4 -3 Q6 0 4 3 M7 -6 Q11 0 7 6"/>
  </g>
  <g class="service-icon icon-response" transform="translate(525 385)">
    <circle r="14"/>
    <path class="glyph" d="M-9 2 L-6 -3 L6 -3 L9 2 L9 6 L-9 6 Z"/>
    <rect class="glyph" x="-2" y="-7" width="4" height="3"/>
    <circle cx="-5" cy="7" r="1.8" class="glyph" style="stroke:none"/>
    <circle cx="5" cy="7" r="1.8" class="glyph" style="stroke:none"/>
  </g>

  <!-- website -->
  <text class="web-address" x="403" y="440">www.birchguard.ie</text>
</svg>
</body>
</html>
```